Drink Coaster Design

We will be providing reusable drink coaster for sports bars. The coasters are 4" by 4" with rounded corners. You can see the coasters at this link:
https://www.trayvillemart.example/4-white-square-80-pt-customizable-paper-coaster-case/712KPLM6T93.html. We want the coasters to be impressive and lead customers to our web site and our twitter account.
I have included one design created for us but it does not look impressive. We provide information to sports bettors who use our service to decide which games to bet on in college and professional football and basketball. You can see our web site at www.zenithwageranalytics.example. You can see our twitter account at https://twitter.com/zenithforecast. I have attached several different logos. The goal is to drive traffic to our web site and our twitter account. The design needs to be a conversation "starter" and needs to be impressive. Please visit our web site to understand what we do and to see our key selling points

```html
<!DOCTYPE html>
<html lang="en">
<head>
<meta charset="utf-8">
<title>Zenith Wager Analytics – Coasters</title>
<link rel="stylesheet" href="https://fonts.googleapis.com/css2?family=Anton&family=Rajdhani:wght@700&display=swap">
<style>
  :root {
    --red: #e30d2e;
    --green: #46b166;
    --dark: #232b26;
    --brown: #3a231f;
    --field-a: #3f8f45;
    --field-b: #5c9a3e;
    --page: #ffffff;
  }
  html, body {
    margin: 0;
    width: 1200px;
    height: 581px;
    overflow: hidden;
    background: var(--page);
  }
  .coasters { display: block; width: 1200px; height: 581px; }
  .headline { font-family: "Anton", "Impact", sans-serif; }
  .headline-shadow { fill: var(--dark); }
  .headline-red { fill: var(--red); }
  .headline-green { fill: var(--green); }
  .brand-name {
    font-family: "Rajdhani", "Arial Narrow", sans-serif;
    font-weight: 700;
    font-size: 34px;
    fill: var(--green);
  }
  .band-text {
    font-family: "Rajdhani", "Arial Narrow", sans-serif;
    font-weight: 700;
    font-size: 18px;
    letter-spacing: 0;
  }
  .band-text-green { fill: var(--green); }
  .band-text-red { fill: var(--red); }
</style>
</head>
<body>
<svg class="coasters" viewBox="0 0 1200 581" xmlns="http://www.w3.org/2000/svg">
  <defs>
    <clipPath id="coaster-left-clip"><rect width="597" height="548"/></clipPath>
    <clipPath id="coaster-right-clip"><rect width="550" height="548"/></clipPath>
    <linearGradient id="football-photo-tone" x1="0" y1="0" x2="1" y2="1">
      <stop offset="0" stop-color="#3e4a45"/>
      <stop offset="0.35" stop-color="var(--field-a)"/>
      <stop offset="0.7" stop-color="#9a9c93"/>
      <stop offset="1" stop-color="var(--field-b)"/>
    </linearGradient>
    <linearGradient id="basketball-photo-tone" x1="0" y1="0" x2="1" y2="1">
      <stop offset="0" stop-color="var(--brown)"/>
      <stop offset="0.5" stop-color="#6b3a33"/>
      <stop offset="0.8" stop-color="#a8584e"/>
      <stop offset="1" stop-color="#4a2a25"/>
    </linearGradient>
    <path id="left-band-line" d="M44,385 C170,505 400,530 585,395"/>
    <path id="right-band-line" d="M40,400 C170,505 380,530 545,405"/>
  </defs>

  <!-- Football coaster -->
  <g class="coaster coaster-football" transform="translate(20,17)" clip-path="url(#coaster-left-clip)">
    <rect class="photo-area" width="597" height="548" fill="url(#football-photo-tone)"
          role="img" aria-label="Photo of a football being kicked on a grass pitch"/>

    <path class="band band-main" fill="var(--red)"
          d="M0,225 C120,400 300,470 420,470 C500,470 560,430 597,345 L597,440 C540,520 460,545 380,545 C230,545 90,505 0,440 Z"/>
    <path class="band band-lower" fill="var(--red)"
          d="M0,460 C120,530 260,548 330,548 L0,548 Z M597,440 L597,548 L470,548 C530,520 570,490 597,440 Z"/>

    <text class="brand-name" x="26" y="62" textLength="180" lengthAdjust="spacingAndGlyphs">ZENITH</text>

    <g class="headline">
      <text class="headline-shadow" x="227" y="152" font-size="138" textLength="333" lengthAdjust="spacingAndGlyphs">YOU</text>
      <text class="headline-red" x="222" y="148" font-size="138" textLength="333" lengthAdjust="spacingAndGlyphs">YOU</text>
      <text class="headline-shadow" x="119" y="238" font-size="79" textLength="163" lengthAdjust="spacingAndGlyphs">CAN</text>
      <text class="headline-red" x="115" y="234" font-size="79" textLength="163" lengthAdjust="spacingAndGlyphs">CAN</text>
      <text class="headline-shadow" x="209" y="399" font-size="144" textLength="326" lengthAdjust="spacingAndGlyphs">WIN</text>
      <text class="headline-red" x="204" y="395" font-size="144" textLength="326" lengthAdjust="spacingAndGlyphs">WIN</text>
    </g>

    <g class="icon-web" fill="none" stroke="var(--green)" stroke-width="2">
      <circle cx="55" cy="400" r="8"/>
      <ellipse cx="55" cy="400" rx="3.5" ry="8"/>
      <line x1="47" y1="400" x2="63" y2="400"/>
    </g>
    <text class="band-text band-text-green" dy="6">
      <textPath href="#left-band-line" startOffset="40">www.ZENITHWAGERANALYTICS.example</textPath>
    </text>
    <text class="band-text band-text-green" dy="6">
      <textPath href="#left-band-line" startOffset="385">● ZENITH FORECAST</textPath>
    </text>
  </g>

  <!-- Basketball coaster -->
  <g class="coaster coaster-basketball" transform="translate(630,17)" clip-path="url(#coaster-right-clip)">
    <rect class="photo-area" width="550" height="548" fill="url(#basketball-photo-tone)"
          role="img" aria-label="Photo of a basketball player shooting in front of an arena crowd"/>

    <path class="band band-main" fill="var(--green)"
          d="M0,280 C90,420 260,480 380,475 C460,470 520,430 550,360 L550,445 C500,520 420,545 350,545 C200,545 70,500 0,450 Z"/>
    <path class="band band-lower" fill="var(--green)"
          d="M550,455 L550,548 L440,548 C490,525 525,495 550,455 Z"/>

    <text class="brand-name" x="29" y="58" textLength="140" lengthAdjust="spacingAndGlyphs">ZENITH</text>

    <g class="headline">
      <text class="headline-shadow" x="211" y="143" font-size="133" textLength="308" lengthAdjust="spacingAndGlyphs">YOU</text>
      <text class="headline-green" x="206" y="139" font-size="133" textLength="308" lengthAdjust="spacingAndGlyphs">YOU</text>
      <text class="headline-shadow" x="212" y="220" font-size="72" textLength="156" lengthAdjust="spacingAndGlyphs">CAN</text>
      <text class="headline-green" x="208" y="216" font-size="72" textLength="156" lengthAdjust="spacingAndGlyphs">CAN</text>
      <text class="headline-shadow" x="227" y="357" font-size="136" textLength="296" lengthAdjust="spacingAndGlyphs">WIN</text>
      <text class="headline-green" x="222" y="353" font-size="136" textLength="296" lengthAdjust="spacingAndGlyphs">WIN</text>
    </g>

    <g class="icon-web" fill="none" stroke="var(--red)" stroke-width="2">
      <circle cx="51" cy="414" r="8"/>
      <ellipse cx="51" cy="414" rx="3.5" ry="8"/>
      <line x1="43" y1="414" x2="59" y2="414"/>
    </g>
    <text class="band-text band-text-red" dy="6">
      <textPath href="#right-band-line" startOffset="40">www.ZENITHWAGERANALYTICS.example</textPath>
    </text>
    <text class="band-text band-text-red" dy="6">
      <textPath href="#right-band-line" startOffset="385">● ZENITH FORECAST</textPath>
    </text>
  </g>
</svg>
</body>
</html>
```